Lift Her Forward, 2019 Save The Date

Please develop a save the date flyer our 4th Annual Lift Her Forward and See Her Rise! This event is focused on maintaining participation and appreciation for women in the design and construction industry.

This unique Forum provides a venue to engage everyone from executives to those just beginning their careers with active, hands-on sessions and vibrant networking with the best and brightest in the A/E/C industry. In our usual Q-TarVM Forum style, Keynotes become table participants and table participants become presenters, encouraging participants to assimilate what they are learning. Join local, state and national leaders and subject matter experts as we candidly explore and address the issues affecting women in our industry.

Industry/Entity Type

Construction

Font styles to use
Sans Serif

Requirements
Must have
• This is a save the date, Must have:
• Q-TarVM Logo
• Title: 4th Annual Lift Her Forward and See Her Rise!
• Date: January 25, 2019
• Location: Harbor Crest Resort and Spa, San Marcos, TX
Nice to have
• A header that can easily be pulled to add to other marketing materials and for use across other platforms (web, etc.).

```html
<!DOCTYPE html>
<html lang="en">
<head>
<meta charset="utf-8">
<title>Lift Her Forward – 2019 Save The Date</title>
<link href="https://fonts.googleapis.com/css2?family=Cinzel:wght@400;700;900&family=Amatic+SC:wght@700&family=Marcellus+SC&display=swap" rel="stylesheet">
<style>
  :root {
    --page-bg: #d9d9d9;
    --sky-top: #6f89c8;
    --sky-mid: #b9c6e6;
    --sky-low: #e6ebf6;
    --ink: #111418;
    --navy: #2a3d92;
    --red: #d6323b;
    --frame: #1c2030;
  }
  * { margin: 0; padding: 0; box-sizing: border-box; }
  html, body { width: 1200px; height: 868px; overflow: hidden; background: var(--page-bg); }
  .flyer {
    position: absolute; left: 310px; top: 23px; width: 580px; height: 822px;
    font-family: "Cinzel", serif; color: var(--ink); text-align: center;
  }
  .flyer__sky {
    position: absolute; inset: 0;
    background:
      radial-gradient(ellipse 60% 25% at 30% 55%, rgba(255,255,255,.55), transparent 70%),
      radial-gradient(ellipse 50% 20% at 75% 70%, rgba(255,255,255,.5), transparent 70%),
      linear-gradient(180deg, var(--sky-top) 0%, var(--sky-mid) 35%, var(--sky-low) 65%, #f3f5fa 100%);
  }
  .flyer__frame { position: absolute; inset: 0; }
  .line { position: absolute; left: 0; width: 100%; white-space: nowrap; }
  .invite { top: 77px; font-size: 12.5px; font-weight: 700; letter-spacing: .3px; }
  .edition { top: 94px; font-size: 22px; font-weight: 700; letter-spacing: 1px; }
  .title { top: 160px; font-size: 40px; font-weight: 900; line-height: 1; letter-spacing: 1px; }
  .title--and { top: 214px; font-weight: 400; }
  .title--big { font-size: 51px; }
  .title--see { top: 264px; }
  .title--rise { top: 324px; }
  .save {
    position: absolute; left: 104px; top: 415px;
    font-family: "Amatic SC", sans-serif; font-weight: 700; font-size: 86px;
    line-height: 1; color: var(--navy); letter-spacing: 2px;
  }
  .date-word {
    position: absolute; left: 104px; top: 496px;
    font-size: 94px; font-weight: 400; color: var(--red); line-height: 1;
  }
  .date-stack { position: absolute; left: 392px; top: 430px; width: 92px; line-height: 1; }
  .date-stack__month { font-size: 44px; color: var(--navy); display: block; }
  .date-stack__day { font-size: 66px; color: var(--red); display: block; margin-top: 2px; }
  .date-stack__year { font-size: 38px; color: var(--navy); display: block; margin-top: 2px; }
  .venue { top: 635px; font-size: 21px; font-weight: 700; color: var(--navy); letter-spacing: .3px; }
  .city { top: 659px; font-family: "Marcellus SC", serif; font-size: 17px; color: var(--navy); }
  .brand { top: 712px; font-size: 24px; font-weight: 700; color: var(--ink); letter-spacing: 2px; }
</style>
</head>
<body>
  <article class="flyer">
    <div class="flyer__sky" role="img" aria-label="Soft blue sky with light clouds"></div>
    <svg class="flyer__frame" width="580" height="822" viewBox="0 0 580 822" aria-hidden="true">
      <g fill="none" stroke="var(--frame)" stroke-width="1.6">
        <line x1="60" y1="40" x2="520" y2="40"/>
        <line x1="60" y1="781" x2="520" y2="781"/>
        <line x1="41" y1="140" x2="41" y2="690"/>
        <line x1="539" y1="140" x2="539" y2="690"/>
        <rect x="34" y="31" width="14" height="14"/>
        <rect x="532" y="31" width="14" height="14"/>
        <rect x="34" y="776" width="14" height="14"/>
        <rect x="532" y="776" width="14" height="14"/>
        <path d="M48 54 H66 M54 48 V66"/>
        <path d="M532 54 H514 M526 48 V66"/>
        <path d="M48 767 H66 M54 773 V755"/>
        <path d="M532 767 H514 M526 773 V755"/>
      </g>
    </svg>
    <p class="line invite">HAVE THE PLEASURE OF INVITING YOU TO OUR</p>
    <p class="line edition">4TH ANNUAL</p>
    <h1>
      <span class="line title">LIFT HER FORWARD</span>
      <span class="line title title--and">AND</span>
      <span class="line title title--big title--see">SEE HER</span>
      <span class="line title title--big title--rise">RISE!</span>
    </h1>
    <p class="save">SAVE THE</p>
    <p class="date-word">DATE</p>
    <p class="date-stack">
      <span class="date-stack__month">JAN</span>
      <span class="date-stack__day">25</span>
      <span class="date-stack__year">2019</span>
    </p>
    <p class="line venue">HARBOR CREST RESORT AND SPA</p>
    <p class="line city">San Marcos, TX</p>
    <p class="line brand">Q-TARVM</p>
  </article>
</body>
</html>
```